Emergency Management Consulting Flyer

Company name: Stone Harbor Emergency Management

I am looking for a postcard design for my emergency management consulting business. I'm looking for something that has some colors and is double sided, on side with the information on services provided and the other side with the contact information. For the main side I'm looking for the following:

How prepared are you?

Services Provided:
Healthcare Preparedness
EOC Support
Emergency Planning
Mitigation Planning
Business Continuity
Disaster Response
Training and Exercises
Project Management
And more

Affordable for small and large organizations
Stand-by contracts available

On the back side, I'm looking for Contact Us section.

Overall I'm looking for something a bit more modern and need to have at least one disaster photo. If you have questions please message me.

Target Market(s)

Government, Healthcare Facilities, Businesses

Industry/Entity Type

Consulting

Requirements
Must have
• Disaster Picture, modern looking
• For the main side I'm looking for the following:
• How prepared are you?
• Services Provided:
• Healthcare Preparedness
• EOC Support
• Emergency Planning
• Mitigation Planning
• Business Continuity
• Disaster Response
• Training and Exercises
• Project Management
• And more
• Affordable for small and large organizations
• Stand-by contracts available

```html
<!DOCTYPE html>
<html lang="en">
<head>
<meta charset="utf-8">
<title>Stone Harbor Emergency Management – Postcard</title>
<link href="https://fonts.googleapis.com/css2?family=Ubuntu:wght@400;500;700&family=Arimo:wght@400;700&display=swap" rel="stylesheet">
<style>
  :root{
    --page:#ecebe8;
    --navy:#1c2f86;
    --blue:#2747a8;
    --bright:#1f78d6;
    --orange:#f08a1c;
    --ink:#222a3a;
    --charcoal:#343434;
    --white:#ffffff;
    --rule:#b9b9b9;
  }
  *{box-sizing:border-box;margin:0;padding:0}
  html,body{width:971px;height:1200px;overflow:hidden}
  body{background:var(--page);position:relative;font-family:"Ubuntu",sans-serif}
  .card{position:absolute;left:134px;width:706px;height:542px;background:var(--white);overflow:hidden;box-shadow:4px 6px 14px rgba(0,0,0,.25)}
  .card--front{top:38px}
  .card--back{top:620px;font-family:"Arimo",sans-serif}
  .card svg.shapes{position:absolute;left:0;top:0}
  .abs{position:absolute}

  /* front */
  .brand{left:300px;top:22px;width:330px;height:52px;display:flex;align-items:center;gap:10px}
  .brand__dot{width:34px;height:34px;border-radius:50%;background:var(--orange);flex:none}
  .brand__name{font-weight:700;font-size:15px;line-height:1.2;color:var(--ink);letter-spacing:.5px;text-transform:uppercase}
  .headline{left:250px;top:94px;width:440px;text-align:center;font-weight:500;font-size:33px;color:var(--orange)}
  .tagline{right:28px;top:326px;text-align:right;font-weight:500;font-size:15px;line-height:19px;color:var(--ink)}
  .services-title{left:352px;top:373px;width:259px;height:39px;border-radius:4px;background:var(--orange);color:var(--white);font-weight:500;font-size:24px;display:flex;align-items:center;justify-content:center}
  .services{list-style:none;font-size:16px;color:#eef2ff}
  .services li{height:24px;display:flex;align-items:center;gap:6px}
  .services li::before{content:"✓";color:var(--orange);font-weight:700;font-size:15px}
  .services--a{left:268px;top:432px}
  .services--b{left:456px;top:432px}

  /* back */
  .about{left:32px;top:48px;width:170px;color:var(--white)}
  .about h2{font-size:20px;font-weight:700;margin-bottom:8px}
  .about p{font-size:14.5px;line-height:17.5px}
  .address{left:32px;color:var(--white)}
  .address h3{font-size:19px;font-weight:700;line-height:22px}
  .address p{font-size:15px;line-height:18px}
  .address--1{top:250px}
  .address--2{top:320px}
  .call{left:0;top:404px;width:230px;height:112px;background:linear-gradient(90deg,#1a55b8,#1f8be6);color:var(--white);padding:10px 0 0 28px}
  .call h3{font-size:23px;font-weight:700;line-height:26px}
  .call .phone{font-size:23px;font-weight:700;line-height:28px}
  .call .web{font-size:17px;line-height:24px;margin-top:2px}
  .back-brand{left:400px;top:58px;width:130px;display:flex;flex-direction:column;align-items:center;gap:6px}
  .back-brand .brand__dot{width:44px;height:44px}
  .back-brand .brand__name{font-family:"Arimo",sans-serif;font-size:12px;text-align:center;color:var(--navy)}
  .stamp{left:531px;top:37px;width:140px;height:106px;border:1px solid var(--rule)}
  .addr-line{left:415px;width:256px;height:1px;background:var(--rule)}
</style>
</head>
<body>

<section class="card card--front">
  <svg class="shapes" width="706" height="542" viewBox="0 0 706 542">
    <defs>
      <linearGradient id="bandGrad" x1="0" y1="0" x2="1" y2="1">
        <stop offset="0" stop-color="#2f55c4"/>
        <stop offset="1" stop-color="#1c2f86"/>
      </linearGradient>
      <linearGradient id="photoGrad" x1="0" y1="0" x2="0" y2="1">
        <stop offset="0" stop-color="#b9c5c9"/>
        <stop offset=".55" stop-color="#6f7b80"/>
        <stop offset="1" stop-color="#3f5560"/>
      </linearGradient>
      <linearGradient id="circleGrad" x1="0" y1="0" x2="1" y2="1">
        <stop offset="0" stop-color="#9aa7b4"/>
        <stop offset="1" stop-color="#5b6670"/>
      </linearGradient>
    </defs>
    <rect width="706" height="542" fill="#f1f1f3"/>
    <!-- services band -->
    <polygon points="222,368 706,368 706,542 146,542" fill="url(#bandGrad)"/>
    <!-- top right corner stripe -->
    <polygon points="650,0 706,0 706,40 668,80" fill="var(--navy)"/>
    <polygon points="290,0 330,0 360,80 320,80" fill="#d7dbe6" opacity=".6"/>
    <!-- chevron stripes -->
    <polygon points="258,0 278,0 338,203 190,542 170,542 314,203" fill="var(--blue)"/>
    <polyline points="292,0 352,203 206,542" fill="none" stroke="var(--navy)" stroke-width="3"/>
    <!-- hero photo -->
    <polygon role="img" aria-label="Photo: a person wading through floodwater carrying a child on their back" points="0,0 240,0 296,203 148,542 0,542" fill="url(#photoGrad)"/>
    <!-- circle photos -->
    <g role="img" aria-label="Photo: people reacting to a disaster">
      <circle cx="363" cy="225" r="64" fill="var(--blue)"/>
      <circle cx="363" cy="225" r="58" fill="url(#circleGrad)"/>
    </g>
    <g role="img" aria-label="Photo: rescue workers carrying a stretcher">
      <circle cx="606" cy="225" r="64" fill="var(--blue)"/>
      <circle cx="606" cy="225" r="58" fill="url(#circleGrad)"/>
    </g>
    <g role="img" aria-label="Photo: responders treating an injured person">
      <circle cx="483" cy="225" r="72" fill="var(--navy)"/>
      <circle cx="483" cy="225" r="65" fill="url(#circleGrad)"/>
    </g>
  </svg>

  <div class="abs brand">
    <span class="brand__dot"></span>
    <span class="brand__name">Stone Harbor Emergency Management</span>
  </div>
  <h1 class="abs headline">How prepared are you?</h1>
  <p class="abs tagline">Affordable for small and large organizations<br>Stand-by contracts available</p>
  <h2 class="abs services-title">Services Provided</h2>
  <ul class="abs services services--a">
    <li>EOC Support</li>
    <li>Mitigation Planning</li>
    <li>Disaster Response</li>
    <li>Project Management</li>
  </ul>
  <ul class="abs services services--b">
    <li>Healthcare Preparedness</li>
    <li>Emergency Planning</li>
    <li>Business Continuity</li>
    <li>Training and Exercises</li>
  </ul>
</section>

<section class="card card--back">
  <svg class="shapes" width="706" height="542" viewBox="0 0 706 542">
    <defs>
      <linearGradient id="stripeGrad" x1="0" y1="0" x2="1" y2="0">
        <stop offset="0" stop-color="#1c2f86"/>
        <stop offset="1" stop-color="#1f8be6"/>
      </linearGradient>
    </defs>
    <polygon points="198,0 216,0 372,265 216,542 198,542 354,265" fill="url(#stripeGrad)"/>
    <polygon points="0,0 192,0 318,265 192,542 0,542" fill="var(--charcoal)"/>
    <polyline points="180,0 338,265 180,542" fill="none" stroke="#ffffff" stroke-width="4"/>
    <polygon points="284,190 324,265 284,340 300,265" fill="var(--navy)"/>
  </svg>

  <div class="abs about">
    <h2>ABOUT US</h2>
    <p>Lorem ipsum dolor sit amet, consectetur adipiscing elit. Aliquam in ex vitae tellus auctor aliquet. Morbi eget tellus a sapien pellentesque sollicitudin. Aliquam sit amet metus libero.</p>
  </div>
  <div class="abs address address--1">
    <h3>Address Line 1</h3>
    <p>Lorem ipsum dolor sit</p>
  </div>
  <div class="abs address address--2">
    <h3>Address Line 2</h3>
    <p>Lorem ipsum dolor sit</p>
  </div>
  <div class="abs call">
    <h3>CALL US</h3>
    <p class="phone">1800-555-014</p>
    <p class="web">www.stoneharborem.com</p>
  </div>

  <div class="abs back-brand">
    <span class="brand__dot"></span>
    <span class="brand__name">Stone Harbor Emergency Management</span>
  </div>
  <div class="abs stamp"></div>
  <div class="abs addr-line" style="top:311px"></div>
  <div class="abs addr-line" style="top:356px"></div>
  <div class="abs addr-line" style="top:400px"></div>
</section>

</body>
</html>
```